Varnick Earthworks and Septic needs a flyer to submit to contractors to offer our services

I need a sleek profession one page full color high gloss document showcasing our services to give to Mobile Home Companies and contractors that need our services.

Target Market(s)

Home Builders. Mobile Home Salesmen. People Building new homes.

Industry/Entity Type

Construction

Font styles to use
Serif
Sans Serif

Requirements
Must have
• Phone Number. Email address. Logo. Services offered: Mobile Home Pads, Meter Pole Placement and Connection, Waterline Connection, On Site Septic System Installs
Should not have
• Jokes, Nothing trying to be cute

```html
<!DOCTYPE html>
<html lang="en">
<head>
<meta charset="UTF-8">
<title>Varnick Earthworks and Septic – Services Flyer</title>
<link href="https://fonts.googleapis.com/css2?family=Archivo+Black&family=Poppins:wght@400;600;700&display=swap" rel="stylesheet">
<style>
  :root {
    --backdrop: #d9d9d9;
    --paper: #ffffff;
    --ink: #111111;
    --navy: #0f4f84;
    --brand-navy: #16478f;
    --red-dark: #3a0f0f;
    --red: #8a2a24;
    --soil-light: #c99a63;
    --soil-dark: #7a5633;
    --sky: #3f7fd0;
    --concrete: #cfcfcf;
    --white: #ffffff;
  }
  * { margin: 0; padding: 0; box-sizing: border-box; }
  html, body {
    width: 1200px; height: 1200px; overflow: hidden;
    background: var(--backdrop);
  }
  .flyer {
    position: absolute; left: 209px; top: 47px;
    width: 782px; height: 1106px;
    background: var(--paper);
    overflow: hidden;
    font-family: "Poppins", sans-serif;
  }
  .flyer-shapes { position: absolute; inset: 0; width: 100%; height: 100%; }
  .brand {
    position: absolute; left: 392px; top: 78px; width: 322px;
    text-align: center; color: var(--brand-navy);
    font-family: "Poppins", sans-serif; font-weight: 700;
  }
  .brand-name { font-size: 30px; line-height: 36px; text-transform: uppercase; }
  .brand-phone { font-size: 30px; line-height: 40px; margin-top: 6px; }
  .services-title {
    position: absolute; left: 44px; top: 250px;
    font-family: "Archivo Black", sans-serif;
    font-size: 52px; line-height: 54px; color: var(--ink);
    text-transform: uppercase; letter-spacing: 0.5px;
  }
  .services-list {
    position: absolute; left: 44px; top: 388px; width: 420px;
    list-style: none; color: var(--ink);
    font-size: 22px; line-height: 29px;
  }
  .services-list li { position: relative; padding-left: 20px; margin-bottom: 11px; }
  .services-list li::before { content: "•"; position: absolute; left: 0; }
  .contact {
    position: absolute; left: 52px; top: 980px;
    list-style: none; color: var(--white); font-size: 20px; line-height: 30px;
  }
  .contact li { display: flex; align-items: center; gap: 14px; margin-bottom: 10px; }
  .contact svg { width: 20px; height: 20px; fill: var(--white); }
</style>
</head>
<body>
  <main class="flyer">
    <svg class="flyer-shapes" viewBox="0 0 626 885" preserveAspectRatio="none" aria-hidden="false">
      <defs>
        <linearGradient id="corner-red" x1="0" y1="0" x2="1" y2="0">
          <stop offset="0" stop-color="var(--red-dark)"/>
          <stop offset="1" stop-color="var(--red)"/>
        </linearGradient>
        <linearGradient id="excavation" x1="0" y1="0" x2="0" y2="1">
          <stop offset="0" stop-color="#5f7a4a"/>
          <stop offset="0.3" stop-color="var(--soil-light)"/>
          <stop offset="1" stop-color="var(--soil-dark)"/>
        </linearGradient>
        <linearGradient id="tank-lift" x1="0" y1="0" x2="0" y2="1">
          <stop offset="0" stop-color="var(--sky)"/>
          <stop offset="0.6" stop-color="var(--concrete)"/>
          <stop offset="1" stop-color="#7a8a5a"/>
        </linearGradient>
      </defs>
      <polygon class="corner-accent" points="0,0 303,0 243,135 0,51" fill="url(#corner-red)"/>
      <polygon class="contact-band" points="0,580 488,885 0,885" fill="var(--navy)"/>
      <polygon class="photo-excavation" role="img" aria-label="Photo of an excavator beside a mobile home and a worker in a freshly dug septic pit"
               points="438,253 626,316 626,880 253,681" fill="url(#excavation)"/>
      <polygon class="photo-tank" role="img" aria-label="Photo of a concrete septic tank being lifted into place"
               points="138,503 271,546 223,680 95,615" fill="url(#tank-lift)"/>
    </svg>

    <div class="brand">
      <div class="brand-name">Varnick Earthworks<br>&amp; Septic</div>
      <div class="brand-phone">903.555.0147</div>
    </div>

    <h1 class="services-title">Services<br>Offered:</h1>

    <ul class="services-list">
      <li>Mobile Home Pads</li>
      <li>Meter Pole Placement<br>and Connection</li>
      <li>Waterline Connection</li>
      <li>On Site Septic System Installs</li>
    </ul>

    <ul class="contact">
      <li>
        <svg viewBox="0 0 24 24" aria-hidden="true"><path d="M6.6 10.8a15.1 15.1 0 0 0 6.6 6.6l2.2-2.2a1 1 0 0 1 1-.25 11.4 11.4 0 0 0 3.6.57 1 1 0 0 1 1 1V20a1 1 0 0 1-1 1A17 17 0 0 1 3 4a1 1 0 0 1 1-1h3.5a1 1 0 0 1 1 1c0 1.25.2 2.45.57 3.57a1 1 0 0 1-.25 1z"/></svg>
        <span>555 014 7720</span>
      </li>
      <li>
        <svg viewBox="0 0 24 24" aria-hidden="true"><path d="M3 5h18a1 1 0 0 1 1 1v12a1 1 0 0 1-1 1H3a1 1 0 0 1-1-1V6a1 1 0 0 1 1-1zm9 7.2L20 7H4z"/></svg>
        <span>info@varnickearthworks.com</span>
      </li>
    </ul>
  </main>
</body>
</html>
```